One page financial canvas needed

I am in the process of developing a financial planning process that uses a one page canvas as a tool for financial education and to explain simple and complex financial strategies to clients. I have the layout and content sorted, just need a hand making it look professional.

It should be a fairly simple project and i have attached a very rough hand drawn canvas showing the desired layout and content. Please feel free to be creative with the design keeping in mind this layout has been chosen to achieve certain outcomes.

Target Market(s)

25-45 Year old Homeowners who are interested in taking better care of the finances

Industry/Entity Type

Financial

Colors

Designer to choose colors to be used in the design.

Requirements
Must have
• very close to the layout in the attached file

```html
<!DOCTYPE html>
<html lang="en">
<head>
<meta charset="utf-8">
<title>Financial Planning Canvas</title>
<link rel="stylesheet" href="https://fonts.googleapis.com/css2?family=Nunito+Sans:wght@400;600&family=Oswald:wght@600&display=swap">
<style>
:root{
  --goals-bg:#b9eaef;
  --goals-ink:#2a7fa0;
  --money-bg:#d3ead3;
  --money-panel:#e0efe0;
  --money-ink:#2e9370;
  --people-bg:#dadff2;
  --people-ink:#6b2f8f;
  --people-band:#7b3f9e;
  --time-band:#4e2f86;
  --time-bg:#d3d3d3;
  --white:#ffffff;
  --divider:#dfe5e5;
}
*{box-sizing:border-box;margin:0;padding:0}
html,body{width:1200px;height:834px;overflow:hidden}
body{position:relative;background:var(--time-bg);font-family:"Nunito Sans",Arial,sans-serif}
.zone{position:absolute;top:0;height:742px}
.zone-goals{left:0;width:300px;background:var(--goals-bg)}
.zone-money{left:300px;width:600px;background:var(--money-bg)}
.zone-people{left:900px;width:300px;background:var(--people-bg)}
.band{position:absolute;top:742px;height:12px}
.band-goals{left:0;width:300px;background:var(--goals-ink)}
.band-money{left:300px;width:600px;background:var(--money-ink)}
.band-people{left:900px;width:300px;background:var(--people-band)}
.band-time{position:absolute;top:754px;left:0;width:1200px;height:13px;background:var(--time-band)}
.panel{position:absolute;background:var(--money-panel)}
.label{position:absolute;height:47px;background:var(--white);display:flex;align-items:center;font-size:16px;letter-spacing:.2px}
.label .text{flex:1;padding:0 14px}
.label .icon{width:58px;height:100%;display:flex;align-items:center;justify-content:center;border-left:1px solid var(--divider)}
.label .icon.lead{border-left:none;border-right:1px solid var(--divider)}
.label.right .text{text-align:right}
.label::after{content:"";position:absolute;top:100%;border-left:11px solid transparent;border-right:11px solid transparent;border-top:11px solid var(--white)}
.label.tip-left::after{left:15px}
.label.tip-right::after{right:15px}
.ink-goals{color:var(--goals-ink)}
.ink-money{color:var(--money-ink)}
.ink-people{color:var(--people-ink)}
.cashflow{position:absolute;left:543px;top:306px;width:114px;height:114px;border-radius:50%;background:var(--money-bg);display:flex;align-items:center;justify-content:center}
.cashflow span{width:98px;height:98px;border-radius:50%;background:var(--money-ink);color:var(--white);font-family:"Oswald",Impact,sans-serif;font-weight:600;font-size:23px;line-height:23px;letter-spacing:1px;display:flex;align-items:center;justify-content:center;text-align:center}
.wealth{position:absolute;left:521px;top:683px;width:150px;height:75px;border-radius:75px 75px 0 0;background:var(--money-ink);color:var(--white);font-size:20px;text-align:center;padding-top:32px}
.time{position:absolute;left:10px;top:777px;width:199px;height:47px;background:var(--white);display:flex;align-items:center;color:var(--time-band);font-size:16px}
.time::after{content:"";position:absolute;left:100%;top:12px;border-top:12px solid transparent;border-bottom:12px solid transparent;border-left:12px solid var(--white)}
.time .icon{width:55px;height:100%;display:flex;align-items:center;justify-content:center;border-right:1px solid var(--divider)}
.time .text{padding-left:12px}
</style>
</head>
<body>
<div class="zone zone-goals"></div>
<div class="zone zone-money"></div>
<div class="zone zone-people"></div>
<div class="band band-goals"></div>
<div class="band band-money"></div>
<div class="band band-people"></div>
<div class="band-time"></div>

<div class="panel" style="left:315px;top:63px;width:281px;height:267px"></div>
<div class="panel" style="left:605px;top:63px;width:281px;height:267px"></div>
<div class="panel" style="left:315px;top:392px;width:281px;height:266px"></div>
<div class="panel" style="left:605px;top:392px;width:281px;height:266px"></div>

<div class="label tip-left ink-goals" style="left:10px;top:10px;width:281px">
  <span class="text">GOALS</span>
  <span class="icon"><svg width="36" height="36" viewBox="0 0 36 36" fill="none" stroke="var(--goals-ink)" stroke-width="4"><circle cx="16" cy="20" r="13"/><circle cx="16" cy="20" r="6"/><path d="M16 20 L31 5" stroke-width="3"/><path d="M27 3 L33 3 L33 9" stroke-width="3"/></svg></span>
</div>

<div class="label tip-left ink-money" style="left:315px;top:10px;width:281px">
  <span class="icon lead"><svg width="36" height="32" viewBox="0 0 36 32" fill="var(--money-ink)"><ellipse cx="18" cy="19" rx="14" ry="10"/><rect x="9" y="24" width="5" height="7" rx="1"/><rect x="22" y="24" width="5" height="7" rx="1"/><rect x="30" y="15" width="5" height="6" rx="2"/><circle cx="18" cy="5" r="5"/></svg></span>
  <span class="text">INCOME</span>
</div>

<div class="label right tip-right ink-money" style="left:605px;top:10px;width:281px">
  <span class="text">EXPENSESS</span>
  <span class="icon"><svg width="36" height="28" viewBox="0 0 36 28" fill="none" stroke="var(--money-ink)" stroke-width="2.5"><rect x="2" y="2" width="28" height="18" rx="1"/><path d="M6 24 H34 V6"/><circle cx="16" cy="11" r="5"/></svg></span>
</div>

<div class="label tip-left ink-money" style="left:315px;top:339px;width:233px">
  <span class="icon lead" style="width:55px"><svg width="30" height="34" viewBox="0 0 30 34" fill="var(--money-ink)"><path d="M10 2 H20 L17 8 H13 Z"/><path d="M12 9 H18 C26 14 29 22 27 28 C26 32 22 33 15 33 C8 33 4 32 3 28 C1 22 4 14 12 9 Z"/><text x="15" y="28" font-size="14" text-anchor="middle" fill="#fff" font-family="Arial,sans-serif" font-weight="700">$</text></svg></span>
  <span class="text">ASSETS</span>
</div>

<div class="label right tip-right ink-money" style="left:650px;top:339px;width:236px">
  <span class="text">DEBT</span>
  <span class="icon" style="width:55px"><svg width="36" height="28" viewBox="0 0 36 28" fill="none" stroke="var(--money-ink)" stroke-width="2.5"><rect x="2" y="8" width="26" height="17" rx="2"/><path d="M2 13 H28"/><path d="M8 4 L31 2 L34 18 L30 19"/></svg></span>
</div>

<div class="cashflow"><span>CASH<br>FLOW</span></div>
<div class="wealth">WEALTH</div>

<div class="label tip-left ink-people" style="left:911px;top:10px;width:269px">
  <span class="text">FEARS</span>
  <span class="icon" style="width:66px"><svg width="30" height="34" viewBox="0 0 30 34" fill="var(--people-ink)"><path d="M14 1 C22 1 28 7 28 14 C28 19 25 22 24 25 V33 H10 V28 H5 C4 28 4 27 4 26 V22 L1 20 L4 15 C4 7 8 1 14 1 Z"/><text x="16" y="19" font-size="14" text-anchor="middle" fill="#fff" font-family="Arial,sans-serif" font-weight="700">?</text></svg></span>
</div>

<div class="label tip-left ink-people" style="left:911px;top:262px;width:269px">
  <span class="text">FRUSTRATIONS</span>
  <span class="icon" style="width:66px"><svg width="30" height="34" viewBox="0 0 30 34" fill="var(--people-ink)"><circle cx="13" cy="6" r="5"/><path d="M8 12 C5 18 4 26 8 31 H22 L24 28 L16 26 L14 19 L22 27 L25 24 L15 13 Z"/></svg></span>
</div>

<div class="label tip-left ink-people" style="left:911px;top:505px;width:269px">
  <span class="text">PARTNERS</span>
  <span class="icon" style="width:66px"><svg width="34" height="32" viewBox="0 0 34 32" fill="var(--people-ink)"><circle cx="6" cy="5" r="4"/><circle cx="17" cy="4" r="4"/><circle cx="28" cy="5" r="4"/><rect x="2" y="10" width="8" height="15" rx="2"/><rect x="13" y="9" width="8" height="22" rx="2"/><rect x="24" y="10" width="8" height="15" rx="2"/></svg></span>
</div>

<div class="time">
  <span class="icon"><svg width="30" height="32" viewBox="0 0 30 32" fill="none" stroke="var(--time-band)" stroke-width="3"><circle cx="15" cy="18" r="11"/><path d="M11 3 H19 M15 3 V7 M15 18 L19 13"/></svg></span>
  <span class="text">TIME</span>
</div>
</body>
</html>
```